Biz Cards, Letterhead
Pls Use Imagination and Refer to Logo Attached. Completely open to ideas. You're the creative ones!
Biz Cards, Letterhead - Consulting
Creative Brief
Simple
Corinne M Dashelt
President & CEO
28516 Belvorne Court Lewes, DE 19958
CDashelt@TheDasheltGroup.example
Don't have to have the text on the back of the card but it is a possibility. Overall, the idea is to be cutting edge, innovative, professional, yet simple. Thanks!
Supply Chain Solutions....Providing Innovation, Automation, & Optimization.

```html
<!DOCTYPE html>
<html lang="en">
<head>
<meta charset="utf-8">
<title>The Dashelt Group – Business Card</title>
<link rel="stylesheet" href="https://fonts.googleapis.com/css2?family=Crimson+Text:ital,wght@0,400;0,600;0,700;1,400&display=swap">
<style>
  :root {
    --backdrop: #e9e6e1;
    --card: #ffffff;
    --navy: #0d1d6e;
    --sky: #3a8de0;
    --sky-light: #8fc4f2;
    --ink: #2b2b2b;
    --rule: #9aa3b5;
    --white: #ffffff;
  }
  * { box-sizing: border-box; margin: 0; padding: 0; }
  html, body {
    width: 1200px; height: 780px; overflow: hidden;
    background: var(--backdrop);
    font-family: "Crimson Text", Georgia, serif;
  }
  .card {
    position: absolute; left: 100px; top: 105px;
    width: 1000px; height: 570px;
    background: var(--card);
    border-radius: 34px;
    overflow: hidden;
    box-shadow: 0 6px 22px rgba(0,0,0,.18);
  }
  .card__band { position: absolute; left: 0; top: 0; width: 1000px; height: 230px; }
  .holder {
    position: absolute; right: 56px; top: 34px; text-align: right; color: var(--white);
  }
  .holder__name { font-size: 40px; font-weight: 700; line-height: 1; }
  .holder__title { font-size: 26px; font-style: italic; margin-top: 6px; }

  .brand {
    position: absolute; left: 150px; top: 225px; width: 440px;
    display: flex; align-items: center; gap: 16px;
    border-bottom: 3px solid var(--sky);
    padding-bottom: 12px;
  }
  .brand__dot { width: 34px; height: 34px; border-radius: 50%; background: var(--navy); flex: none; }
  .brand__name { font-size: 46px; font-weight: 600; color: var(--navy); letter-spacing: 1px; white-space: nowrap; }
  .brand__rule { position: absolute; left: 150px; top: 306px; width: 440px; height: 1px; background: var(--sky-light); }

  .address {
    position: absolute; right: 590px; top: 402px; text-align: right;
    font-size: 25px; line-height: 1.25; color: var(--ink); font-style: normal;
  }
  .divider { position: absolute; left: 430px; top: 372px; width: 2px; height: 150px; background: var(--rule); }

  .contacts { position: absolute; left: 448px; top: 370px; list-style: none; }
  .contacts li { display: flex; align-items: center; gap: 10px; font-size: 24px; line-height: 1.3; color: var(--ink); }
  .contacts svg { width: 22px; height: 22px; flex: none; }
</style>
</head>
<body>
  <article class="card">
    <svg class="card__band" viewBox="0 0 1000 230" aria-hidden="true">
      <path d="M0 0 H1000 V150 C760 70 360 60 0 130 Z" fill="var(--navy)"/>
      <path d="M0 130 C360 60 760 70 1000 150 V178 C760 92 360 84 0 146 Z" fill="var(--sky)"/>
      <path d="M0 146 C360 84 760 92 1000 178 V186 C760 102 360 94 0 154 Z" fill="var(--sky-light)"/>
    </svg>

    <header class="holder">
      <p class="holder__name">Corinne M Dashelt</p>
      <p class="holder__title">President &amp; CEO</p>
    </header>

    <div class="brand">
      <span class="brand__dot"></span>
      <span class="brand__name">The Dashelt Group</span>
    </div>
    <div class="brand__rule"></div>

    <address class="address">
      28516 Belvorne Court<br>Harwell Bay, ST 00000
    </address>
    <div class="divider"></div>

    <ul class="contacts">
      <li>
        <svg viewBox="0 0 24 24"><rect x="7" y="2" width="10" height="20" rx="2" fill="var(--navy)"/><rect x="9" y="5" width="6" height="10" fill="var(--white)"/></svg>
        443.555.0182
      </li>
      <li>
        <svg viewBox="0 0 24 24"><rect x="3" y="9" width="18" height="12" rx="2" fill="var(--navy)"/><path d="M4 9 C6 3 18 3 20 9" stroke="var(--navy)" stroke-width="3" fill="none"/></svg>
        253.555.0147
      </li>
      <li>
        <svg viewBox="0 0 24 24"><circle cx="12" cy="12" r="4" fill="none" stroke="var(--navy)" stroke-width="2.5"/><path d="M16 12 V14 a3 3 0 0 0 5 0 V12 a9 9 0 1 0 -4 7.5" fill="none" stroke="var(--navy)" stroke-width="2.5"/></svg>
        CDashelt@TheDasheltGroup.example
      </li>
      <li>
        <svg viewBox="0 0 24 24"><circle cx="12" cy="12" r="9" fill="none" stroke="var(--navy)" stroke-width="2"/><ellipse cx="12" cy="12" rx="4" ry="9" fill="none" stroke="var(--navy)" stroke-width="1.6"/><path d="M3 12 H21 M5 7 H19 M5 17 H19" stroke="var(--navy)" stroke-width="1.4"/></svg>
        www.TheDasheltGroup.example
      </li>
    </ul>
  </article>
</body>
</html>
```